coffee bag design

i would like you to sketch our logo (plum logo) . we want to design a coffee bag. i'll send a logo and an example of how i want it. also all the information to include.
the logo is plum logo i uploaded it i want it to be as the example i attached (sketched logo) with a background. be as creative as you can. you can show me different background ideas behind the sketched logo
font to use : bigNoodleTitling
Target Market(s)
coffee industry
Industry/Entity Type
f&b
Font styles to use
Other font styles liked:
- bignoodletitling
Colors
Designer to choose only greyscale colors for use in the design.
Requirements
Must have
- the information i attached "about the signature blend"
Nice to have
- sketches
Should not have

```html
<!DOCTYPE html>
<html lang="en">
<head>
<meta charset="utf-8">
<title>Plum Coffee – Signature Blend Bag Dieline</title>
<link rel="stylesheet" href="https://fonts.googleapis.com/css2?family=Bebas+Neue&family=Quicksand:wght@500;700&family=Arimo&display=swap">
<style>
  :root {
    --sheet: #ffffff;
    --bag: #f3f3f3;
    --ink: #141414;
    --band: #232323;
    --teal: #17ada0;
    --teal-dark: #138f84;
    --dim: #222222;
    --accent-red: #e3262b;
    --white: #ffffff;
  }
  * { margin: 0; padding: 0; box-sizing: border-box; }
  html, body { width: 1200px; height: 897px; overflow: hidden; background: var(--sheet); }
  .canvas { position: relative; width: 1200px; height: 897px; font-family: "Quicksand", sans-serif; color: var(--ink); }
  .abs { position: absolute; line-height: 1; white-space: nowrap; }

  .panel { position: absolute; top: 133px; width: 464px; height: 749px; background: var(--bag); overflow: hidden; }
  .panel--front { left: 115px; }
  .panel--back { left: 596px; }
  .panel .band { position: absolute; left: 0; bottom: 0; width: 100%; height: 143px; background: var(--band); }

  .dimension-layer { position: absolute; inset: 0; pointer-events: none; }
  .dim-label { font-family: "Arimo", sans-serif; color: var(--dim); text-align: center; }
  .dim-small { font-size: 12px; line-height: 14px; }
  .dim-large { font-size: 23px; }
  .dim-mid { font-size: 19px; }
  .vertical { transform: rotate(-90deg); transform-origin: center; }
  .vertical-cw { transform: rotate(90deg); transform-origin: center; }
  .weight-tag { color: var(--accent-red); font-family: "Arimo", sans-serif; font-weight: 700; font-size: 26px; }

  .hero-art { position: absolute; left: 0; top: 129px; width: 464px; height: 311px;
    background: radial-gradient(ellipse at 50% 55%, #9a9a9a 0%, #c9c9c9 45%, rgba(243,243,243,0) 75%); }

  .wordmark { font-family: "Bebas Neue", sans-serif; color: var(--ink); letter-spacing: 2px; text-align: center; }
  .est { font-family: "Bebas Neue", sans-serif; letter-spacing: 0.45em; text-align: center; color: var(--ink); }
  .blend-title { font-family: "Bebas Neue", sans-serif; letter-spacing: 3px; text-align: center; }

  .spec-table { position: absolute; left: 79px; top: 580px; width: 307px; height: 112px; background: var(--teal); }
  .spec-table .row { position: absolute; left: 18px; width: 269px; font-family: "Bebas Neue", sans-serif; color: var(--white); font-size: 13px; letter-spacing: 0.3px; }
  .spec-table .row .label { position: absolute; left: 0; }
  .spec-table .row .value { position: absolute; left: 92px; line-height: 14px; }
  .spec-table .rule { position: absolute; left: 18px; width: 269px; height: 1px; background: var(--white); }
  .spec-table .divider { position: absolute; left: 90px; top: 8px; width: 1px; height: 96px; background: var(--white); }

  .band-caption { color: var(--white); font-size: 13px; text-align: center; width: 100%; left: 0; }

  .info-card { position: absolute; left: 27px; top: 0; width: 163px; height: 328px; background: var(--white); box-shadow: 0 0 4px rgba(0,0,0,0.15); }
  .info-card p { position: absolute; top: 222px; left: 0; width: 100%; text-align: center; font-size: 13px; line-height: 17px; font-weight: 500; }

  .section-head { font-weight: 700; color: var(--teal); font-size: 20px; }
  .body-copy { font-size: 13px; line-height: 17px; font-weight: 500; text-align: justify; white-space: normal; }
  .badge-row { position: absolute; left: 212px; top: 186px; }
  .distributor { color: var(--white); text-align: center; width: 100%; left: 0; }
  .distributor .head { color: var(--teal); font-weight: 700; font-size: 17px; }
  .distributor .line { font-size: 16px; margin-top: 3px; font-weight: 500; }
</style>
</head>
<body>
<main class="canvas">

  <!-- FRONT PANEL -->
  <section class="panel panel--front">
    <div class="hero-art" role="img" aria-label="Hand-drawn sketch illustration of a gentleman with coffee splash and coffee branches with cherries"></div>
    <div class="band"></div>
    <div class="abs wordmark" style="left:0;width:464px;top:430px;font-size:92px;">PLUM</div>
    <div class="abs est" style="left:0;width:464px;top:514px;font-size:21px;">EST 2017</div>
    <div class="abs blend-title" style="left:0;width:464px;top:543px;font-size:36px;">SIGNATURE BLEND</div>

    <div class="spec-table">
      <div class="divider"></div>
      <div class="row" style="top:10px;"><span class="label">VARIETY</span><span class="value">CATURRA, CATUAI, BOURBON, SIDAMA</span></div>
      <div class="rule" style="top:27px;"></div>
      <div class="row" style="top:31px;"><span class="label">PROCESS</span><span class="value">NATURAL AND WASHED</span></div>
      <div class="rule" style="top:47px;"></div>
      <div class="row" style="top:52px;"><span class="label">ATTITUDE</span><span class="value">1,500 TO 2,000 MASL</span></div>
      <div class="rule" style="top:70px;"></div>
      <div class="row" style="top:76px;"><span class="label">TASTE NOTES</span><span class="value">RED BERRIES, ORANGE, CARAMEL,<br>DARK CHOCOLATE, WINTER AND FLORAL</span></div>
    </div>

    <div class="abs band-caption" style="top:712px;">100% NATURAL COFFEE</div>
  </section>

  <!-- BACK PANEL -->
  <section class="panel panel--back">
    <div class="band"></div>
    <div class="info-card">
      <div class="abs wordmark" style="left:0;width:163px;top:147px;font-size:48px;">PLUM</div>
      <div class="abs est" style="left:0;width:163px;top:199px;font-size:13px;">EST 2017</div>
      <p>Lorem Ipsum is<br>simply dummy text<br>of the printing and<br>typesetting industry.<br>Lorem Ipsum.</p>
    </div>

    <div class="abs blend-title" style="left:217px;width:203px;top:140px;font-size:32px;color:var(--teal);">SIGNATURE BLEND</div>
    <svg class="abs" style="left:219px;top:176px;" width="200" height="2"><line x1="0" y1="1" x2="200" y2="1" stroke="#9a9a9a" stroke-dasharray="4 3"/></svg>

    <svg class="badge-row" width="210" height="70" role="img" aria-label="Product quality seals">
      <g fill="none" stroke="var(--teal)" stroke-width="2">
        <circle cx="33" cy="33" r="32" fill="var(--white)"/>
        <circle cx="33" cy="33" r="18" fill="var(--teal)"/>
        <circle cx="104" cy="33" r="32" fill="var(--white)"/>
        <circle cx="104" cy="33" r="14" fill="var(--teal)"/>
        <circle cx="175" cy="33" r="32" fill="var(--white)"/>
        <circle cx="175" cy="33" r="18" fill="var(--teal)"/>
      </g>
    </svg>

    <div class="abs section-head" style="left:212px;top:263px;">STORING</div>
    <div class="abs body-copy" style="left:212px;top:282px;width:210px;">Lorem Ipsum is simply dummy text of the printing and typesetting industry. Lorem Ipsum.</div>

    <div class="abs wordmark" style="left:0;width:483px;top:350px;font-size:86px;">PLUM</div>
    <div class="abs est" style="left:0;width:471px;top:433px;font-size:21px;">EST 2017</div>

    <div class="abs section-head" style="left:0;width:460px;text-align:center;top:467px;">BREWING</div>
    <div class="abs body-copy" style="left:45px;top:487px;width:372px;text-align:justify;text-align-last:center;">Lorem Ipsum is simply dummy text of the printing and typesetting industry. Lorem Ipsum has been the industry's standard dummy text ever since the 1500s, when an unknown printer took a galley of type and scrambled it to make a type specimen book. It has survived not only five centuries, but also the leap into electronic typesetting.</div>

    <div class="abs distributor" style="top:631px;">
      <div class="head">DISTRIBUTED BY</div>
      <div class="line">Plum Coffee Company LLC</div>
      <div class="line">555-014-2290 &nbsp;|&nbsp; hello@plumroast.com</div>
    </div>
    <svg class="abs" style="left:99px;top:697px;" width="272" height="3"><line x1="0" y1="1.5" x2="272" y2="1.5" stroke="var(--white)" stroke-width="1.5" stroke-dasharray="1.5 2.5"/></svg>
    <div class="abs band-caption" style="top:712px;">100% NATURAL COFFEE</div>
  </section>

  <!-- DIELINE & DIMENSIONS -->
  <svg class="dimension-layer" width="1200" height="897" viewBox="0 0 1200 897">
    <defs>
      <marker id="arrow" viewBox="0 0 8 8" refX="7" refY="4" markerWidth="6" markerHeight="6" orient="auto-start-reverse">
        <path d="M0,0 L8,4 L0,8 z" fill="var(--dim)"/>
      </marker>
    </defs>
    <g stroke="var(--ink)" stroke-width="1.3" stroke-dasharray="4 4" fill="none">
      <line x1="142" y1="133" x2="142" y2="739"/><line x1="552" y1="133" x2="552" y2="739"/>
      <line x1="623" y1="133" x2="623" y2="739"/><line x1="1033" y1="133" x2="1033" y2="739"/>
      <line x1="115" y1="222" x2="579" y2="222"/><line x1="115" y1="242" x2="579" y2="242"/><line x1="115" y1="261" x2="579" y2="261"/>
      <line x1="596" y1="222" x2="1060" y2="222"/><line x1="596" y1="242" x2="1060" y2="242"/><line x1="596" y1="261" x2="1060" y2="261"/>
    </g>
    <g fill="var(--ink)">
      <path d="M115,199 L122,204 L115,209 z"/><path d="M579,199 L572,204 L579,209 z"/>
      <path d="M596,199 L603,204 L596,209 z"/><path d="M1060,199 L1053,204 L1060,209 z"/>
    </g>
    <g stroke="var(--dim)" stroke-width="1" fill="none">
      <!-- top widths -->
      <line x1="115" y1="58" x2="115" y2="120"/><line x1="579" y1="58" x2="579" y2="120"/>
      <line x1="142" y1="96" x2="142" y2="120"/><line x1="552" y1="96" x2="552" y2="120"/>
      <line x1="117" y1="78" x2="577" y2="78" marker-start="url(#arrow)" marker-end="url(#arrow)"/>
      <line x1="144" y1="108" x2="550" y2="108" marker-start="url(#arrow)" marker-end="url(#arrow)"/>
      <line x1="129" y1="46" x2="129" y2="106" marker-start="url(#arrow)" marker-end="url(#arrow)"/>
      <line x1="566" y1="46" x2="566" y2="106" marker-start="url(#arrow)" marker-end="url(#arrow)"/>
      <line x1="596" y1="58" x2="596" y2="120"/><line x1="1060" y1="58" x2="1060" y2="120"/>
      <line x1="623" y1="96" x2="623" y2="120"/><line x1="1033" y1="96" x2="1033" y2="120"/>
      <line x1="598" y1="78" x2="1058" y2="78" marker-start="url(#arrow)" marker-end="url(#arrow)"/>
      <line x1="625" y1="108" x2="1031" y2="108" marker-start="url(#arrow)" marker-end="url(#arrow)"/>
      <line x1="610" y1="46" x2="610" y2="106" marker-start="url(#arrow)" marker-end="url(#arrow)"/>
      <line x1="1047" y1="46" x2="1047" y2="106" marker-start="url(#arrow)" marker-end="url(#arrow)"/>
      <!-- left heights -->
      <line x1="46" y1="133" x2="115" y2="133"/><line x1="46" y1="882" x2="115" y2="882"/>
      <line x1="70" y1="135" x2="70" y2="880" marker-start="url(#arrow)" marker-end="url(#arrow)"/>
      <line x1="93" y1="135" x2="93" y2="198" marker-start="url(#arrow)" marker-end="url(#arrow)"/>
      <line x1="70" y1="200" x2="115" y2="200"/>
      <line x1="115" y1="204" x2="56" y2="204" marker-end="url(#arrow)"/>
      <line x1="92" y1="739" x2="115" y2="739"/>
      <line x1="97" y1="741" x2="97" y2="880" marker-start="url(#arrow)" marker-end="url(#arrow)"/>
      <!-- right heights -->
      <line x1="1060" y1="133" x2="1102" y2="133"/><line x1="1060" y1="882" x2="1102" y2="882"/>
      <line x1="1062" y1="222" x2="1102" y2="222"/><line x1="1062" y1="261" x2="1102" y2="261"/>
      <line x1="1084" y1="135" x2="1084" y2="220" marker-start="url(#arrow)" marker-end="url(#arrow)"/>
      <line x1="1084" y1="224" x2="1084" y2="259" marker-start="url(#arrow)" marker-end="url(#arrow)"/>
      <line x1="1084" y1="263" x2="1084" y2="880" marker-start="url(#arrow)" marker-end="url(#arrow)"/>
      <line x1="1086" y1="245" x2="1128" y2="245" marker-start="url(#arrow)" marker-end="url(#arrow)"/>
    </g>
  </svg>

  <div class="abs dim-label dim-small" style="left:110px;top:19px;width:40px;">7.5mm<br>Seal</div>
  <div class="abs dim-label dim-small" style="left:542px;top:19px;width:40px;">7.5mm<br>Seal</div>
  <div class="abs dim-label dim-small" style="left:590px;top:19px;width:40px;">7.5mm<br>Seal</div>
  <div class="abs dim-label dim-small" style="left:1027px;top:19px;width:40px;">7.5mm<br>Seal</div>
  <div class="abs weight-tag" style="left:171px;top:51px;">150g</div>
  <div class="abs dim-label dim-large" style="left:247px;top:52px;">Total Width_130mm</div>
  <div class="abs dim-label dim-large" style="left:728px;top:52px;">Total Width_130mm</div>
  <div class="abs dim-label dim-mid" style="left:312px;top:89px;">115mm</div>
  <div class="abs dim-label dim-mid" style="left:793px;top:89px;">115mm</div>

  <div class="abs dim-label vertical dim-large" style="left:-46px;top:495px;width:210px;">Total Height_210mm</div>
  <div class="abs dim-label vertical dim-small" style="left:64px;top:160px;width:40px;">19mm</div>
  <div class="abs dim-label dim-small" style="left:20px;top:194px;width:38px;">Cut<br>Mark</div>
  <div class="abs dim-label vertical dim-small" style="left:48px;top:784px;width:110px;line-height:14px;">40mm_Bottom<br>Gusset</div>

  <div class="abs dim-label vertical-cw dim-mid" style="left:1075px;top:168px;width:50px;">25mm</div>
  <div class="abs dim-label dim-small" style="left:1130px;top:232px;width:52px;font-size:14px;line-height:17px;">11mm<br>Zipper</div>
  <div class="abs dim-label vertical-cw dim-mid" style="left:1069px;top:563px;width:62px;">174mm</div>

</main>
</body>
</html>
```